ちょっと急いでおりまして、
当方デザインをする時間がないので、
アウトソーシングしたいと思います。

文章、と構成だけを作りましたので、
宜しければ、お願い致します。

TAVELIA JAPAN で使用する、
お客さまにブランディングするための、
青嶺かやどり の パンフレットです。

PDFで、説明文を記載致しますので、
また見ておいて下さい。

画像素材も、添付させて頂きます。
「青嶺かやどり・かやたまご」を使うフォントは、
明朝体です。アウトラインしたデータも
添付いたします。それを活用下さい。

A4サイズ (裏・表)
両面カラーでで作っていただけると幸いです。

※もしかすると、A0サイズで引き伸ばしてつかうかもしれません。
どうぞよろしくお願い致します。

何か御不明な点がございましたら、お気軽に
ご質問ください。

当社青嶺かやどりの商品ページです。
参考にして下さい。
http://item.shopmarket-example.jp/poultry-hoshino/20004681/

青嶺かやどり協議会の ページです。
http://www.kayadori-example.com/
素材を添付いたします。レイヤーを使っておりますので、分解してください。
このページにある

の画像のような感じで、要約していただけると
幸いです。
画像を追加いたしました。
タイトルが、4Aに なってました。

すみません。A4ポスターです。
循環型の 111 のような 感じで、

ぐるっと 回る ように わかりやすく つくって頂けると幸いです。
かやどりの アニメーションデータは、

aiファイル イラストレーターの
かやたまご に 入っています。

レイヤーで組んでいますが、それを修正して作って下さい。
素材 画像を追加いたしました。
素材追加いたします。

111、222、333、444画像は、見本画像です。
イメージの参考になるかも?と思いまして、
かやどり からでる 副産物の 鶏糞堆肥もっこもこ の画像を 追加いたします。

裏側の、一番重要な情報を綺麗にまとめてくださりました。
そして、私達が やっていることに対して 共感頂けたことが大きかったです。
少し修正頂きたい部分がありますので、御連絡頂けると幸いです。

皆様 急な対応、ありがとうございます。
10件も御応募いただけるとは思っても居なかったのと、
そして、みなさんからの提案が本当に良かったので。
こちらとしても 悩ましかったです。
御提案くださった皆様。本当に、ありがとうございましたm(__)m

```html
<!DOCTYPE html>
<html lang="ja">
<head>
<meta charset="utf-8">
<title>青嶺かやどり・かやたまご</title>
<link rel="stylesheet" href="https://fonts.googleapis.com/css2?family=Shippori+Mincho+B1:wght@700;800&family=M+PLUS+Rounded+1c:wght@500;700;800&display=swap">
<style>
  :root {
    --bg-top: #f7bcd5;
    --bg-mid: #fbd7e6;
    --bg-bottom: #f2a3c4;
    --brand-pink: #e5007f;
    --deep-pink: #d6006f;
    --ring-pink: #f07fb0;
    --ink: #231815;
    --white: #ffffff;
    --meat: #f3b6a6;
    --meat-shadow: #e58f86;
    --gold: #d9ad43;
    --red: #e60033;
  }
  * { box-sizing: border-box; margin: 0; padding: 0; }
  html, body { width: 849px; height: 1200px; overflow: hidden; }
  body { background: var(--bg-bottom); }
  .poster {
    position: relative; width: 849px; height: 1200px; overflow: hidden;
    background: linear-gradient(180deg, var(--bg-top) 0%, var(--bg-mid) 45%, var(--bg-top) 75%, var(--bg-bottom) 100%);
    font-family: "M PLUS Rounded 1c", sans-serif; color: var(--ink);
  }
  .title {
    position: absolute; top: 30px; left: 18px; height: 600px;
    writing-mode: vertical-rl; font-family: "Shippori Mincho B1", serif;
    font-weight: 800; font-size: 90px; line-height: 1.05; letter-spacing: 2px;
  }
  .title .region { font-size: 68px; }
  .title .bird { font-size: 80px; }
  .tagline-en {
    position: absolute; top: 200px; left: 218px; width: 92px;
    font-size: 9.5px; line-height: 1.35; color: var(--ink);
  }
  .tagline-en .brand-en { display: block; margin-top: 6px; color: var(--brand-pink); font-weight: 700; }
  .mascot-egg { position: absolute; top: 330px; left: 230px; }
  .hero { position: absolute; top: 28px; left: 312px; }
  .feed-banner {
    position: absolute; top: 40px; left: 462px; width: 378px; height: 40px;
    background: var(--brand-pink); border-radius: 20px; color: var(--white);
    font-weight: 700; font-size: 19px; line-height: 40px; text-align: center;
    box-shadow: 0 0 0 3px var(--white);
  }
  .feed-banner .accent { color: #ffe04d; }
  .awards { position: absolute; top: 400px; left: 608px; }
  .headline {
    position: absolute; top: 632px; left: 40px; width: 770px;
    font-size: 33px; font-weight: 800; color: var(--deep-pink);
    padding-bottom: 10px; border-bottom: 3px dotted var(--ring-pink);
  }
  .headline .dark { color: var(--ink); }
  .points { position: absolute; top: 700px; left: 40px; width: 445px; list-style: none; }
  .points li { display: flex; gap: 12px; margin-bottom: 18px; font-size: 20px; font-weight: 700; line-height: 1.35; }
  .points .num { color: var(--brand-pink); font-size: 30px; font-weight: 800; line-height: 1; min-width: 40px; }
  .illustration-bird { position: absolute; top: 830px; left: 400px; }
  .illustration-flower { position: absolute; top: 985px; left: 60px; }
  .council { position: absolute; bottom: 42px; left: 30px; font-size: 17px; font-weight: 700; }
  .council-url { position: absolute; bottom: 20px; left: 30px; font-size: 12px; color: var(--ink); }
</style>
</head>
<body>
<main class="poster">
  <h1 class="title"><span class="region">青嶺</span><span class="bird">かやどり</span><br>かやたまご</h1>

  <p class="tagline-en">It is so delicious. You will be happy if you have it. Everyone says it is the best chicken and egg. Try it!
    <span class="brand-en">Seirei Kayadori<br>Kayatamago</span></p>

  <svg class="mascot-egg" width="60" height="50" role="img" aria-label="卵のマスコットキャラクター">
    <ellipse cx="30" cy="25" rx="28" ry="22" fill="#fff6e0"/>
  </svg>

  <svg class="hero" width="500" height="500" viewBox="0 0 500 500">
    <defs>
      <radialGradient id="meatFill" cx="50%" cy="45%" r="60%">
        <stop offset="0%" stop-color="#f8cbbd"/>
        <stop offset="70%" stop-color="var(--meat)"/>
        <stop offset="100%" stop-color="var(--meat-shadow)"/>
      </radialGradient>
    </defs>
    <circle cx="250" cy="250" r="248" fill="var(--white)"/>
    <circle cx="250" cy="250" r="240" fill="var(--ring-pink)"/>
    <circle cx="250" cy="250" r="226" fill="url(#meatFill)" role="img" aria-label="かやどりの生肉の写真"/>
  </svg>

  <div class="feed-banner"><span class="accent">青嶺</span>の梅酢を飼料にした贅沢な鶏</div>

  <svg class="awards" width="230" height="130">
    <circle cx="58" cy="66" r="56" fill="var(--red)" stroke="var(--gold)" stroke-width="5"/>
    <circle cx="170" cy="62" r="56" fill="var(--gold)" stroke="var(--white)" stroke-width="4"/>
  </svg>

  <h2 class="headline"><span class="dark">青嶺かやどり、</span>最大の自慢は<span>健康</span>！</h2>

  <ol class="points">
    <li><span class="num">01</span><span>青嶺の梅酢を飼料にした贅沢な鶏。</span></li>
    <li><span class="num">02</span><span>梅酢効果で免疫力アップ、抵抗力アップ！<br>病気になりにくくなった健康な鶏。</span></li>
    <li><span class="num">03</span><span>地鶏のように赤い肉で、皮や内臓や骨も色艶がピカピカ！</span></li>
    <li><span class="num">04</span><span>梅酢効果でコクがあり適度な弾力があるのにやわらかく臭みがない。</span></li>
  </ol>

  <svg class="illustration-flower" width="130" height="125" role="img" aria-label="梅の花のイラスト">
    <circle cx="65" cy="62" r="58" fill="#f06aa3"/>
  </svg>

  <svg class="illustration-bird" width="440" height="370" role="img" aria-label="かやどりのキャラクターと卵のイラスト">
    <ellipse cx="250" cy="170" rx="160" ry="160" fill="#ffffff" opacity="0.92"/>
    <ellipse cx="60" cy="320" rx="40" ry="45" fill="#ffffff" opacity="0.92"/>
    <ellipse cx="400" cy="325" rx="36" ry="42" fill="#ffffff" opacity="0.92"/>
  </svg>

  <p class="council">青嶺かやどり協議会</p>
  <p class="council-url">http://www.kayadori-example.com/</p>
</main>
</body>
</html>
```